Ledgerwise Reach - B2B Demand Generation Website Project

We need a fully functional website for www.ledgerwisereach.example. We are a B2B Demand Generation company, based in London, working with companies such as QRT, VKD, Norvex, Brindlow, Tarvo generating them sales leads for their sales teams. We run this through digital marketing newsletter promotions and have a network of websites. Content syndication, data, demand generation, online marketing. Our logo has just been redone (attached) and we have a holding page already which i would like to use the style / colours. Our logo is bright and vibrant but i dont want the site to be a rainbow. We are expensive, classy, professorial, B2B, intelligent.

Home
About Us
Our Services
Prospora & QA Technology
Intent Data
Testimonials
Contact Us
Updates

Target Market(s)

B2B Marketers (QRT, Velquarion, Tarvo, VKD, Opal Reach, Driftmoor, Harlow Quantis, Technology Companies, Data Companies, Marketing Teams, Tumbleden.

Industry/Entity Type

Marketing

Coding

Coded - Design and coding required

Number of Pages Required

5+ page

Font styles to use
Sans Serif

Requirements
Must have
• Home
About Us
Our Services
Prospora & QA Technology
Intent Data
Testimonials
Contact Us

Simple Pages.

Look classy, intelligent, data experts. I like the video homepages were the image moves at the top. Very soft animation.
Nice to have
• Websites i like:

https://www.vkd.example/
https://www.brevantor.example/
https://www.plumfieldsites.example.co.uk/

Ledgerwise Reach - The Demand Generation Company
Should not have
• Glimpsevault crap images

```html
<!DOCTYPE html>
<html lang="en">
<head>
<meta charset="utf-8">
<title>Ledgerwise Reach - The Demand Generation Company</title>
<link rel="stylesheet" href="https://fonts.googleapis.com/css2?family=Questrial&family=Montserrat:wght@400;500;600;700;800;900&display=swap">
<style>
:root{
  --navy:#1b4f9a;
  --red:#c1272d;
  --ink:#2b2b2b;
  --muted:#555;
  --pink:#e6a5a8;
  --sky:#e9f1fb;
  --grey:#f2f2f2;
  --footer:#142340;
  --white:#fff;
}
*{box-sizing:border-box;margin:0;padding:0}
html,body{width:1200px;height:4304px;overflow:hidden}
body{position:relative;font-family:"Montserrat",sans-serif;color:var(--ink);background:var(--white)}
.abs{position:absolute}
.label{position:absolute;font-family:"Questrial",sans-serif;color:var(--red);font-size:19px;letter-spacing:1.5px;text-transform:uppercase;line-height:1}
.label::before{content:"";display:inline-block;width:20px;height:1.5px;background:var(--red);vertical-align:middle;margin-right:8px}
.label.both::after{content:"";display:inline-block;width:20px;height:1.5px;background:var(--red);vertical-align:middle;margin-left:8px}
.heading{position:absolute;font-family:"Questrial",sans-serif;color:var(--navy);font-size:30px;line-height:35px;font-weight:400}
.body-text{position:absolute;font-size:10.5px;line-height:19px;color:var(--muted);text-align:justify;letter-spacing:.2px}
.body-text p+p{margin-top:9px}
.btn{position:absolute;height:34px;border-radius:17px;background:var(--red);color:var(--white);font-size:10px;font-weight:700;letter-spacing:1px;display:flex;align-items:center;justify-content:center;gap:8px;text-transform:uppercase}
.btn svg{width:16px;height:8px}
.btn.ghost{background:var(--white);color:var(--red)}
/* hero */
.hero{position:absolute;left:0;top:0;width:1200px;height:605px;background:radial-gradient(circle at 30% 45%,#2a78d4 0%,#1a5cbf 35%,#0f3f96 70%,#0a2f7a 100%)}
.brand{position:absolute;left:158px;top:26px;display:flex;flex-direction:column;align-items:center;color:var(--white)}
.brand .dot{width:42px;height:42px;border-radius:50%;border:2px solid rgba(255,255,255,.85)}
.brand .name{font-size:24px;font-weight:500;margin-top:6px;letter-spacing:-.3px}
.brand .tag{font-size:7px;letter-spacing:.4px;margin-top:2px}
.menu{position:absolute;left:1014px;top:36px;width:26px}
.menu span{display:block;height:2px;background:var(--white);margin-bottom:6px}
.hero-text{position:absolute;right:164px;top:195px;text-align:right}
.hero-text .kicker{font-family:"Questrial",sans-serif;color:var(--red);font-size:22px;letter-spacing:1.5px}
.hero-text .kicker::after{content:"";display:inline-block;width:22px;height:1.5px;background:var(--red);vertical-align:middle;margin-left:8px}
.hero-text h1{font-family:"Questrial",sans-serif;color:var(--white);font-weight:400;font-size:37px;line-height:43px;margin-top:12px}
.down{position:absolute;left:580px;top:518px;width:40px;height:40px;border-radius:50%;background:var(--white);display:flex;align-items:center;justify-content:center}
/* stats */
.stat{position:absolute;border:1.5px solid var(--pink);text-align:center}
.stat b{display:block;font-weight:900;font-size:30px;color:#111;letter-spacing:1px;margin-top:28px}
.stat i{display:block;width:20px;height:1px;background:#999;margin:14px auto 12px}
.stat span{font-size:16px;line-height:24px;color:#222}
/* clients */
.clients{position:absolute;left:0;top:1111px;width:1200px;height:370px;background:var(--sky)}
.client{position:absolute;top:212px;font-weight:800;color:var(--navy);font-size:30px;letter-spacing:2px;display:flex;align-items:center;gap:10px;transform:translateX(-50%)}
.client .sq{width:12px;height:12px;background:var(--navy)}
.dots{position:absolute;display:flex;gap:5px;transform:translateX(-50%)}
.dots span{width:9px;height:9px;border-radius:50%;background:#9a9a9a}
.dots span.on{background:var(--red)}
/* services */
.card{position:absolute;top:1676px;width:248px;height:356px;background:var(--white);border:1.5px solid #bdbdbd;box-shadow:0 3px 8px rgba(0,0,0,.12);padding:70px 20px 0 22px}
.card.active{border:2px solid var(--red);box-shadow:none}
.card h3{font-family:"Questrial",sans-serif;font-weight:400;font-size:16.5px;line-height:22px;color:#111;height:58px;white-space:nowrap}
.card.active h3{color:var(--red)}
.card p{font-size:9px;line-height:18.5px;color:#555;text-align:justify}
.card .more{position:absolute;right:24px;top:274px;font-size:9.5px;color:#222}
.card.active .more{color:var(--red)}
/* qa */
.qa{position:absolute;left:0;top:2203px;width:1200px;height:558px;background:var(--grey)}
.testi{position:absolute;left:0;top:3362px;width:1200px;height:569px;background:var(--grey)}
.tcard{position:absolute;top:262px;width:356px;height:161px;background:var(--white);border:1px solid var(--pink);padding:56px 25px 0}
.tcard .avatar{position:absolute;left:25px;top:-29px;width:58px;height:58px;border-radius:50%;background:#d3d3d3}
.tcard .quote{position:absolute;right:24px;top:18px;color:var(--red);font-family:"Montserrat",sans-serif;font-weight:900;font-size:46px;line-height:46px}
.tcard h4{font-size:12px;font-weight:600;color:#111}
.tcard h4 small{font-weight:400;font-size:9px;color:#555}
.tcard p{font-size:9.5px;line-height:15.5px;color:#555;margin-top:12px}
/* footer */
.footer{position:absolute;left:0;top:3931px;width:1200px;height:373px;background:var(--footer);color:#fff}
.fcol{position:absolute;top:70px;font-size:10px}
.fcol h5{font-size:10.5px;font-weight:700;letter-spacing:.5px}
.fcol h5::after{content:"";display:block;width:24px;height:1px;background:#fff;margin-top:7px}
.fcol ul{list-style:none;margin-top:24px}
.fcol li{line-height:20.5px}
.fcol .red{color:var(--red);font-weight:700;font-size:8.5px;letter-spacing:.8px}
.subscribe{margin-top:10px;width:219px;height:31px;border:1px solid #fff;display:flex;align-items:center;justify-content:space-between;padding:0 10px;font-size:9.5px}
.contact li{display:flex;gap:8px;align-items:center;line-height:32px}
.copy{position:absolute;left:160px;top:344px;font-size:9px}
.social{position:absolute;left:952px;top:338px;display:flex;gap:8px}
.social span{width:22px;height:22px;border-radius:50%;border:1.5px solid #fff}
</style>
</head>
<body>

<header class="hero" role="img" aria-label="Abstract blue swirl of dotted rings with a speech-bubble emblem">
  <div class="brand"><div class="dot"></div><div class="name">ledgerwisereach</div><div class="tag">The Demand Generation Company</div></div>
  <div class="menu"><span></span><span></span><span></span></div>
  <div class="hero-text">
    <div class="kicker">LEDGERWISE REACH</div>
    <h1>The Demand Generation<br>Company</h1>
  </div>
  <div class="btn" style="left:732px;top:359px;width:142px">About Us <svg viewBox="0 0 16 8"><path d="M0 4h14M11 1l3 3-3 3" stroke="currentColor" fill="none" stroke-width="1.3"/></svg></div>
  <div class="btn ghost" style="left:894px;top:359px;width:144px">Services <svg viewBox="0 0 16 8"><path d="M0 4h14M11 1l3 3-3 3" stroke="currentColor" fill="none" stroke-width="1.3"/></svg></div>
  <div class="down"><svg width="12" height="14" viewBox="0 0 12 14"><path d="M6 1v11M2 8l4 4 4-4" stroke="#1b4f9a" fill="none" stroke-width="1.5"/></svg></div>
  <svg class="abs" style="left:0;top:535px" width="1200" height="70" viewBox="0 0 1200 70"><path d="M0 50 C400 62 850 40 1200 0 V70 H0 Z" fill="#fff"/></svg>
</header>

<section class="about">
  <div class="label" style="left:162px;top:658px">About Us</div>
  <h2 class="heading" style="left:162px;top:683px">Ledgerwise Reach<br>The Demand Generation<br>Company</h2>
  <div class="body-text" style="left:162px;top:814px;width:365px">
    <p><b style="color:#222">Ledgerwise Reach</b> offers multi-channel demand generation services to publishers and technology vendors through our network of lead generation websites and native speaking telemarketing agents.</p>
    <p>Whether looking for MQL, ABM or BANT campaigns, <b style="color:#222">Ledgerwise Reach</b> can assist you in delivering your demand generation strategy and generate pipeline for your sales teams and/or channel partners.</p>
  </div>
  <div class="btn" style="left:391px;top:1014px;width:135px">About Us <svg viewBox="0 0 16 8"><path d="M0 4h14M11 1l3 3-3 3" stroke="currentColor" fill="none" stroke-width="1.3"/></svg></div>
  <div class="stat" style="left:592px;top:693px;width:208px;height:165px"><b>70,000+</b><i></i><span>Downloads Per<br>Month</span></div>
  <div class="stat" style="left:832px;top:693px;width:208px;height:165px"><b>25,000+</b><i></i><span>Leads Delivered<br>Per Month</span></div>
  <div class="stat" style="left:592px;top:884px;width:448px;height:165px"><b>50+</b><i></i><span>Countries We Can<br>Reach</span></div>
</section>

<section class="clients">
  <div class="label both" style="left:0;width:1200px;text-align:center;top:54px">Who We Work With</div>
  <h2 class="heading" style="left:0;width:1200px;text-align:center;top:82px">People Who Trust Us</h2>
  <div class="client" style="left:251px">QRT</div>
  <div class="client" style="left:483px">TARVO</div>
  <div class="client" style="left:715px"><span class="sq"></span>VKD</div>
  <div class="client" style="left:947px">DUNMORE</div>
  <div class="dots" style="left:600px;top:303px"><span></span><span class="on"></span><span></span></div>
</section>

<section class="services">
  <div class="label" style="left:162px;top:1550px">Our Services</div>
  <h2 class="heading" style="left:162px;top:1576px">What We’re Great At</h2>
  <article class="card active" style="left:160px">
    <h3>Marketing Qualified<br>Leads (MQL)</h3>
    <p>A Marketing Qualified Lead (MQL) is a prospect that has expressed an interest in what your brand has to offer. An MQL has taken the first steps to becoming a customer and is ready to receive ...</p>
    <span class="more">Continue ›</span>
  </article>
  <article class="card" style="left:486px">
    <h3>Account Based Marketing<br>Leads (ABM)</h3>
    <p>ABM is a strategy that directs marketing resources to engaging a specific set of target accounts.<br>Instead of casting a wide net to engage any potential customers...</p>
    <span class="more">Continue ›</span>
  </article>
  <article class="card" style="left:792px">
    <h3>Sales Qualified Lead<br>/ BANT</h3>
    <p>An SQL lead or a BANT lead is a type of lead that expressed a specific interest in a product and service that you have to offer... The difference between marketing qualified leads (MQL) and sales ...</p>
    <span class="more">Continue ›</span>
  </article>
  <div class="btn" style="left:531px;top:2095px;width:137px">View Services <svg viewBox="0 0 16 8"><path d="M0 4h14M11 1l3 3-3 3" stroke="currentColor" fill="none" stroke-width="1.3"/></svg></div>
</section>

<section class="qa">
  <div class="abs" role="img" aria-label="Laptop showing the Prospora project dashboard" style="left:92px;top:131px;width:536px;height:281px;background:linear-gradient(180deg,#e9ecef 0%,#d7dbe0 100%);border-radius:10px"></div>
  <div class="label" style="left:668px;top:97px">QA Technology</div>
  <h2 class="heading" style="left:669px;top:124px">Prospora : Verification<br>Platform from Ledgerwise Reach</h2>
  <div class="body-text" style="left:672px;top:212px;width:369px">
    <p>Prospora is a proprietary lead verification platform from Ledgerwise Reach that aims to sift out invalid leads with questionable or erroneous data. The platform is designed to equip sales teams with accurate, high-quality records in order to improve lead generation, accelerate pipeline and increase revenue.</p>
    <p>Prospora is positioned to quickly identify, validate, and improve lead quality at the point-of-entry by filtering out all leads that do not match required filters, such as job title, company size, etc.</p>
  </div>
  <div class="btn" style="left:907px;top:420px;width:136px">Discover <svg viewBox="0 0 16 8"><path d="M0 4h14M11 1l3 3-3 3" stroke="currentColor" fill="none" stroke-width="1.3"/></svg></div>
</section>

<section class="intent">
  <div class="label" style="left:159px;top:2848px">Intent Data</div>
  <h2 class="heading" style="left:159px;top:2874px">Access To 35 Million<br>Individuals And a Global<br>Behavioural Data Stream</h2>
  <div class="body-text" style="left:159px;top:3004px;width:370px">
    <p>Our relationships with the world’s most important technology &amp; business decisions-makers generate a perpetual stream of global data. With access to 35 million individuals and a global behavioural data stream that is authenticated, timely and contextually relevant, we have one of the industry’s most powerful signals of buyer intent and can fuel your demand-generation marketing strategies globally.</p>
    <p>We support our intent targeting capabilities by partnering with a number of third party intent providers, meaning we are able to target the global data universe to deliver the best and most engaging leads to our partners.</p>
  </div>
  <div class="btn" style="left:396px;top:3238px;width:137px">More Details <svg viewBox="0 0 16 8"><path d="M0 4h14M11 1l3 3-3 3" stroke="currentColor" fill="none" stroke-width="1.3"/></svg></div>
  <div class="abs" role="img" aria-label="Isometric data cubes stacked on a glowing platform" style="left:643px;top:2933px;width:443px;height:342px;background:radial-gradient(ellipse at 50% 55%,#c7e9f2 0%,#e4f5f8 45%,#fff 75%)"></div>
</section>

<section class="testi">
  <div class="label both" style="left:0;width:1214px;text-align:center;top:89px">Testimonials</div>
  <h2 class="heading" style="left:0;width:1214px;text-align:center;top:113px">What our Clients Says<br>About Us</h2>
  <article class="tcard" style="left:159px">
    <div class="avatar" role="img" aria-label="Client portrait"></div><div class="quote">”</div>
    <h4>Alden Marsh <small>/ CEO QRT</small></h4>
    <p>Lorem ipsum dolor sit amet, consectetur adipiscing elit. Donec ut sem elementum, tristique justo quis, varius risus. Vivamus consectetur sapien sodales arcu interdum, at dapibus mi porta.</p>
  </article>
  <article class="tcard" style="left:685px">
    <div class="avatar" role="img" aria-label="Client portrait"></div><div class="quote">”</div>
    <h4>Alden Marsh <small>/ CEO QRT</small></h4>
    <p>Lorem ipsum dolor sit amet, consectetur adipiscing elit. Donec ut sem elementum, tristique justo quis, varius risus. Vivamus consectetur sapien sodales arcu interdum, at dapibus mi porta.</p>
  </article>
  <div class="dots" style="left:600px;top:469px"><span></span><span class="on"></span><span></span></div>
</section>

<footer class="footer">
  <div class="fcol" style="left:160px"><h5>QUICK LINKS</h5><ul><li>Home</li><li>About Us</li><li>Our Services</li><li>Prospora &amp; QA Technology</li><li>Intent Data</li><li>Testimonials</li><li>Contact Us</li></ul></div>
  <div class="fcol" style="left:366px"><h5>CARREERS</h5>
    <ul><li style="line-height:16px">Join our team of exprts, curious<br>and ambition</li><li class="red">EXPLORE OPENINGS →</li></ul>
    <h5 style="margin-top:24px">SUBSCRIBE</h5>
    <div class="subscribe" style="margin-top:22px"><span>Enter you email *</span><span class="red">SEND →</span></div>
  </div>
  <div class="fcol" style="left:675px"><h5>COMPANY</h5><ul style="font-size:9.5px"><li style="line-height:17.5px">Awards</li><li style="line-height:17.5px">Site Map</li><li style="line-height:17.5px">Term &amp; Conditions</li><li style="line-height:17.5px">Support Services</li><li style="line-height:17.5px">Privacy Policy</li><li style="line-height:17.5px">Help</li><li style="line-height:17.5px">Support Services</li><li style="line-height:17.5px">Privacy Policy</li><li style="line-height:17.5px">Help</li></ul></div>
  <div class="fcol contact" style="left:884px"><h5>CONTACT</h5><ul style="margin-top:14px">
    <li><svg width="9" height="12" viewBox="0 0 9 12"><path d="M4.5 11S1 7 1 4.5a3.5 3.5 0 0 1 7 0C8 7 4.5 11 4.5 11z" fill="none" stroke="#c1272d"/></svg>48 Carrow Lane Suite 210</li>
    <li><svg width="11" height="11" viewBox="0 0 11 11"><path d="M2 1l2 0 1 3-1.5 1a6 6 0 0 0 2.5 2.5L7 6l3 1v2c0 1-1 1-1 1A9 9 0 0 1 1 2s0-1 1-1z" fill="none" stroke="#c1272d"/></svg>+001 555-010-2244</li>
    <li><svg width="11" height="9" viewBox="0 0 11 9"><rect x=".5" y=".5" width="10" height="8" fill="none" stroke="#c1272d"/><path d="M.5 .5l5 4 5-4" fill="none" stroke="#c1272d"/></svg>contact@ledgerwisereach.example</li>
    <li><svg width="11" height="11" viewBox="0 0 11 11"><circle cx="5.5" cy="5.5" r="4.8" fill="none" stroke="#c1272d"/><path d="M5.5 3v2.5H7.5" fill="none" stroke="#c1272d"/></svg>From 08:00AM to 18:00PM</li>
  </ul></div>
  <div class="copy">Ledgerwise Reach © 2020. All Rights Reserved</div>
  <div class="social"><span></span><span style="border-color:#c1272d"></span><span></span></div>
</footer>

</body>
</html>
```